New Flyer Design Project

PAGE 1

Change to 8th Annual Copperline Clash and the new date is January 24, 2026

12U, Middle School & High School - add Open 18+

Under Weigh-ins
Early Registration is $25.00
Deadline is January 18, 2026 at 11:59 PM

Regular Registration is $35.00
Deadline is January 21, 2026 at 11:59 PM

Late / On-site Registration is $50.00
Deadline is January 23, 2026 at 5:00 PM
Change 500 to 750

Under Weigh-Ins - Change
January 24, 2025 to January 23, 2026
January 25, 2025 to January 24, 2026

PAGE 2
Change 2024-2025 to 2025-2026

In the Division Line Fix the numbers 1, 2, 3, 4, 5, 6, 7, 8, 9, 10

Change 12/31/2024 to 12/31/2025 where it says "Age As Of"
Change to "Excluding the High School & Open Division"

```html
<!DOCTYPE html>
<html lang="en">
<head>
<meta charset="utf-8">
<title>8th Annual Copperline Clash – Flyer</title>
<link href="https://fonts.googleapis.com/css2?family=Alfa+Slab+One&family=Bebas+Neue&family=Oswald:wght@400;500;600;700&family=Montserrat:wght@400;500;600;700&display=swap" rel="stylesheet">
<style>
:root{
  --backdrop:#b3b3b3;
  --paper:#f2dfbb;
  --paper-edge:#e6cfa3;
  --maroon:#6b0f17;
  --maroon-deep:#4e0910;
  --tan:#c58a3a;
  --tan-light:#efc98f;
  --ink:#2a1510;
  --white:#ffffff;
}
*{margin:0;padding:0;box-sizing:border-box}
html,body{width:1200px;height:875px;overflow:hidden}
body{background:var(--backdrop);position:relative;font-family:"Montserrat",sans-serif;color:var(--ink)}
.page{position:absolute;top:90px;width:497px;height:696px;overflow:hidden;
  background:radial-gradient(ellipse at 40% 35%,var(--paper) 55%,var(--paper-edge) 100%)}
.page--front{left:68px}
.page--back{left:635px}
.abs{position:absolute}

/* titles */
.event-title{font-family:"Alfa Slab One",serif;color:var(--maroon);line-height:1;text-transform:uppercase;letter-spacing:-.5px;white-space:nowrap}
.event-title span{display:block}
.front .event-title{left:28px;top:28px}
.front .event-title span{font-size:27px}
.front .event-title span+span{margin-top:8px}
.event-date{left:28px;top:109px;font-family:"Oswald",sans-serif;font-weight:700;font-size:23px;line-height:1;color:var(--maroon-deep);text-transform:uppercase;letter-spacing:.3px}
.venue{left:28px;top:138px;font-size:10.5px;line-height:1.1;width:300px;display:flex;gap:4px}
.venue svg{flex:none;margin-top:1px}

/* org pennant */
.org-pennant{left:369px;top:0;width:84px;height:120px}
.org-name{left:369px;top:30px;width:84px;text-align:center;font-family:"Oswald",sans-serif;font-weight:700;font-size:15px;color:var(--paper);letter-spacing:1px}
.org-name small{display:block;font-size:5.5px;font-weight:600;letter-spacing:.2px;line-height:1.25;margin:4px auto 0;width:70px}

/* bands */
.mats-band{left:0;top:168px;width:205px;height:24px;background:var(--tan);clip-path:polygon(0 0,88% 0,100% 100%,0 100%);
  font-family:"Oswald",sans-serif;font-weight:600;color:var(--white);font-size:19px;line-height:24px;padding-left:28px}
.schedule-band{left:0;top:192px;width:497px;height:66px;background:var(--maroon);color:var(--white);font-family:"Oswald",sans-serif;padding:6px 0 0 28px}
.schedule-band p{font-size:11px;font-weight:500;line-height:17px;text-transform:uppercase}
.register{display:flex;align-items:center;gap:5px}
.register .url{background:var(--white);color:var(--ink);font-family:"Montserrat",sans-serif;font-size:10px;font-weight:500;border-radius:8px;padding:0 9px;line-height:14px;text-transform:none}
.open-tag{left:244px;top:182px;width:58px;height:64px;background:var(--tan);clip-path:polygon(0 0,100% 0,100% 84%,50% 100%,0 84%);
  text-align:center;color:var(--white);font-family:"Oswald",sans-serif}
.open-tag b{display:block;font-size:13px;font-weight:600;letter-spacing:1px;margin-top:4px}
.open-tag em{display:block;font-style:normal;font-size:24px;font-weight:700;line-height:1;color:var(--maroon-deep)}

/* registration */
.fees{left:28px;top:272px;display:flex;flex-direction:column;gap:8px}
.fee{display:flex;align-items:center;gap:5px;font-family:"Oswald",sans-serif;height:19px;white-space:nowrap}
.fee-label{border:2px solid var(--tan);border-radius:9px;background:var(--paper);font-size:9px;font-weight:500;text-transform:uppercase;padding:0 14px 0 6px;line-height:13px;position:relative;z-index:0}
.fee-price{background:var(--maroon);color:var(--white);font-size:14px;font-weight:600;border-radius:9px;padding:0 6px;line-height:18px;margin-left:-12px;position:relative;z-index:1}
.fee-deadline{background:var(--maroon);color:var(--white);font-size:6px;font-weight:600;border-radius:6px;padding:1px 4px;text-transform:uppercase}
.fee-day{font-size:15px;font-weight:600;color:var(--maroon)}
.fee-day sup{font-size:7px}
.month-tag{background:var(--tan);color:var(--white);font-size:5px;font-weight:700;text-transform:uppercase;line-height:6px;padding:1px 3px;border-radius:2px;text-align:center}
.fee-time{font-size:14px;font-weight:600;color:var(--maroon);border-left:1px solid var(--maroon);padding-left:5px}
.fee-time sup{font-size:7px}

/* weigh-ins */
.weigh-box{left:28px;top:356px;width:440px;height:122px;background:var(--tan);border-radius:14px 0 0 14px}
.weigh-tab{left:44px;top:352px;width:92px;height:32px;background:var(--paper);border-radius:10px 10px 0 0;
  font-family:"Oswald",sans-serif;font-weight:600;color:var(--maroon);font-size:20px;text-align:center;line-height:34px}
.weigh-rows{left:42px;top:388px;display:flex;flex-direction:column;gap:8px;font-family:"Oswald",sans-serif}
.weigh-row{display:flex;align-items:center;gap:6px;height:20px;white-space:nowrap}
.weigh-day{font-size:17px;font-weight:600;color:var(--white);width:28px}
.weigh-day sup{font-size:8px}
.weigh-row .month-tag{background:var(--maroon);font-size:6px;line-height:7px;width:38px}
.weigh-time{background:var(--paper);color:var(--maroon);font-size:10px;font-weight:500;border-radius:8px;padding:0 6px;line-height:16px;margin-left:8px;width:107px;text-align:center}
.weigh-note{color:var(--white);font-size:9.5px;font-weight:500;line-height:11px;text-transform:uppercase}

/* rules */
.rules{left:30px;top:488px;width:272px;font-size:8.4px;line-height:10.6px;color:#3a2418}
.rules p+p{margin-top:9px}

/* footer */
.footer-band{left:0;top:602px;width:497px;height:44px;background:var(--maroon)}
.admission{left:28px;top:593px;display:flex;align-items:center;background:var(--maroon);border-radius:10px;padding-right:12px;font-family:"Oswald",sans-serif;color:var(--white)}
.admission b{background:var(--tan);border-radius:10px;font-size:10.5px;font-weight:500;padding:0 7px;line-height:16px;margin-right:6px;text-transform:uppercase}
.admission span{font-size:12.5px}
.contact{left:28px;top:615px;font-family:"Oswald",sans-serif;color:var(--white);font-size:9.5px;line-height:12px;text-transform:uppercase;font-weight:500}
.contact .row{display:flex;align-items:center;gap:6px}
.hotels{left:28px;top:653px;font-family:"Oswald",sans-serif;color:var(--maroon);font-size:9.5px;font-weight:500;text-transform:uppercase;white-space:nowrap}
.hotels .list{display:flex;gap:6px;margin-top:3px;font-size:6.5px;color:var(--ink)}
.hotels .list span{display:flex;align-items:center;gap:2px}
.hotels .list em{font-style:normal;color:var(--tan)}

/* artwork slots */
.art{position:absolute}
.front .warrior{left:310px;top:140px;width:187px;height:556px;
  background:linear-gradient(180deg,rgba(120,20,24,0) 0%,#6a2a1c 20%,#4b3326 45%,#3a2a20 70%,#2a1b14 100%);
  clip-path:polygon(45% 0,65% 3%,80% 10%,100% 14%,100% 100%,0 100%,12% 60%,25% 40%,30% 18%)}

/* back page */
.back .event-title{left:0;width:497px;top:28px;text-align:center}
.back .event-title span{font-size:30px}
.back .event-title span+span{margin-top:8px}
.classes-title{left:0;width:497px;top:116px;text-align:center;font-family:"Bebas Neue",sans-serif;font-size:35px;line-height:1;color:var(--ink);letter-spacing:-.2px;white-space:nowrap}
.weights{left:29px;top:157px;width:440px}
.grid{display:grid;grid-template-columns:84px repeat(10,35.6px)}
.head-num{background:var(--ink);color:var(--white);font-family:"Oswald",sans-serif;font-size:10px;height:16px;line-height:16px;border-radius:3px 3px 0 0}
.head-num>*{text-align:center;border-left:1px solid #fff}
.head-num>:first-child{text-align:left;padding-left:6px;border:0;font-weight:600}
.head-sub{background:var(--maroon);color:var(--white);font-family:"Montserrat",sans-serif;font-weight:700;font-size:5px;line-height:5.6px;height:28px;text-transform:uppercase;margin-bottom:3px}
.head-sub>*{display:flex;align-items:center;justify-content:center;text-align:center;border-left:1px solid #fff;padding:0 1px}
.head-sub>:first-child{justify-content:flex-start;text-align:left;padding-left:6px;border:0;font-size:5.2px}
.wrow{height:15.5px;font-family:"Oswald",sans-serif;font-size:10.5px;line-height:15.5px}
.wrow>*{text-align:center}
.wrow.light>.v{background:var(--tan-light);color:var(--ink)}
.wrow.dark>.v{background:var(--maroon);color:var(--white)}
.back .warrior{left:0;top:326px;width:134px;height:370px;
  background:linear-gradient(180deg,#8a1b20 0%,#5a3a2a 30%,#3b2a20 65%,#24160f 100%);
  clip-path:polygon(25% 0,55% 4%,70% 18%,100% 40%,100% 100%,0 100%,0 8%)}
.mats{left:125px;top:542px;width:260px;height:76px;background:linear-gradient(135deg,#2c2f36,#1a1c22 60%,#7a2a2a)}
.singlets{left:387px;top:522px;width:86px;height:96px;background:linear-gradient(180deg,#e8dccb,#8c8a94);border-radius:6px}
.awards-band{left:0;top:618px;width:497px;height:78px;background:var(--maroon)}
.awards{left:161px;top:626px;width:320px;color:var(--white)}
.awards h2{font-family:"Montserrat",sans-serif;font-weight:700;font-size:16px;line-height:20px;letter-spacing:.2px;color:var(--paper);text-transform:uppercase;white-space:nowrap}
.awards p{font-size:12.5px;line-height:16px;margin-top:2px}
</style>
</head>
<body>

<!-- PAGE 1 -->
<section class="page page--front front">
  <div class="art warrior" role="img" aria-label="Armoured warrior with crested helmet, red cloak and spear"></div>

  <svg class="abs org-pennant" viewBox="0 0 84 120" aria-hidden="true">
    <polygon points="0,0 84,0 84,120 42,100 0,120" fill="#6b0f17"/>
  </svg>
  <div class="abs org-name">RYWA<small>RIDGEWAY YOUTH WRESTLING ASSOCIATION</small></div>

  <h1 class="abs event-title"><span>8th Annual</span><span>Copperline Clash</span></h1>
  <p class="abs event-date">January 24, 2026</p>
  <p class="abs venue">
    <svg width="9" height="9" viewBox="0 0 10 10"><circle cx="5" cy="5" r="5" fill="#6b0f17"/><path d="M5 2a2 2 0 0 0-2 2c0 1.5 2 4 2 4s2-2.5 2-4a2 2 0 0 0-2-2z" fill="#fff"/></svg>
    <span>Harborview Event Center 418 Maple Ridge Ave, Harborview</span>
  </p>

  <div class="abs schedule-band">
    <p>K-5, 60, 80, 100-Wrestling starts at 8:30 AM</p>
    <p>&amp; 12U, Middle School &amp; High School</p>
    <p class="register">Register @ <span class="url">www.MatRoster.com</span></p>
  </div>
  <div class="abs mats-band">6 MATS</div>
  <div class="abs open-tag"><b>OPEN</b><em>18+</em></div>

  <div class="abs fees">
    <div class="fee"><span class="fee-label">Early Registration</span><span class="fee-price">$25.00</span><span class="fee-deadline">Deadline is</span><span class="fee-day">18<sup>TH</sup></span><span class="month-tag">January<br>2026</span><span class="fee-time">11:59<sup>PM</sup></span></div>
    <div class="fee"><span class="fee-label">Regular Registration</span><span class="fee-price">$35.00</span><span class="fee-deadline">Deadline is</span><span class="fee-day">21<sup>ST</sup></span><span class="month-tag">January<br>2026</span><span class="fee-time">11:59<sup>PM</sup></span></div>
    <div class="fee"><span class="fee-label">Late / On-site Registration</span><span class="fee-price">$50.00</span><span class="fee-deadline">Deadline is</span><span class="fee-day">23<sup>RD</sup></span><span class="month-tag">January<br>2026</span><span class="fee-time">5:00<sup>PM</sup></span></div>
  </div>

  <div class="abs weigh-box"></div>
  <div class="abs weigh-tab">Weigh-Ins</div>
  <div class="abs weigh-rows">
    <div class="weigh-row"><span class="weigh-day">23<sup>RD</sup></span><span class="month-tag">January<br>2026</span><span class="weigh-time">5:00 PM TO 7:00 PM</span><span class="weigh-note">Early weigh-ins-<br>$10 cash due at scale</span></div>
    <div class="weigh-row"><span class="weigh-day">24<sup>TH</sup></span><span class="month-tag">January<br>2026</span><span class="weigh-time">6:00 AM TO 7:30 AM</span><span class="weigh-note">(K-5, 60, 80, 100)</span></div>
    <div class="weigh-row"><span class="weigh-day">24<sup>TH</sup></span><span class="month-tag">January<br>2026</span><span class="weigh-time">11:00 AM TO 12:00 PM</span><span class="weigh-note">(12 &amp; under,<br>MS, &amp; High School)</span></div>
  </div>

  <div class="abs rules">
    <p>Tenths are waived/dropped at weigh-ins, satellite weigh-ins will not be allowed, High school divisions are given 2 lbs, growth allowance, Custom medals will be given to the top 3 individual finishers in each bracket.</p>
    <p>Custom awards will be awarded to the top 4 teams, referee decisions will be final, Birchwood Athletics is not responsible for accidents, injuries, or theft during the Tournament.</p>
  </div>

  <div class="abs footer-band"></div>
  <div class="abs admission"><b>Admission</b><span>$10.00 PER PERSON</span></div>
  <div class="abs contact">
    <div>For more information,</div>
    <div class="row">Contact tournament director Dana Keller
      <svg width="10" height="10" viewBox="0 0 10 10"><circle cx="5" cy="5" r="5" fill="#fff"/><path d="M3.2 2.5l1 1-.5.8a3.5 3.5 0 0 0 2 2l.8-.5 1 1-.6.8C5 7.5 2.5 5 2.5 3.1z" fill="#6b0f17"/></svg>
      (555) 014-0760</div>
  </div>
  <div class="abs hotels">
    <div>Hotels available on-site</div>
    <div class="list">
      <span><em>Lakeside Inn</em> ☎ (555) 013-5000</span>
      <span><em>Cedar Suites</em> ☎ (555) 013-7400</span>
      <span><em>Pinecrest Lodge</em> ☎ (555) 013-8300</span>
    </div>
  </div>
</section>

<!-- PAGE 2 -->
<section class="page page--back back">
  <h1 class="abs event-title"><span>8th Annual</span><span>Copperline Clash</span></h1>
  <h2 class="abs classes-title">2025-2026 RYWA Age &amp; Weight Classes</h2>

  <div class="abs weights">
    <div class="grid head-num"><span>DIVISION</span><span>01</span><span>02</span><span>03</span><span>04</span><span>05</span><span>06</span><span>07</span><span>08</span><span>09</span><span>10</span></div>
    <div class="grid head-sub"><span>Excluding the High School &amp; Open Division<br>12/31/2025</span><span>6 &amp; Under</span><span>8 &amp; Under</span><span>10 &amp; Under</span><span>12 &amp; Under</span><span>Middle School</span><span>Girls K-5</span><span>Girls 6th 8th</span><span>Women's Grades 9-12</span><span>High School Grades 9-12</span><span>Open 18+</span></div>

    <div class="grid wrow light"><i class="v"></i><span class="v">36</span><span class="v">40</span><span class="v">52</span><span class="v">68</span><span class="v">76</span><span class="v">40</span><span class="v">76</span><span class="v">100</span><span class="v">106</span><span class="v">125</span></div>
    <div class="grid wrow dark"><i class="v"></i><span class="v">40</span><span class="v">44</span><span class="v">56</span><span class="v">72</span><span class="v">83</span><span class="v">44</span><span class="v">83</span><span class="v">107</span><span class="v">113</span><span class="v">133</span></div>
    <div class="grid wrow light"><i class="v"></i><span class="v">44</span><span class="v">48</span><span class="v">60</span><span class="v">76</span><span class="v">90</span><span class="v">48</span><span class="v">90</span><span class="v">114</span><span class="v">120</span><span class="v">141</span></div>
    <div class="grid wrow dark"><i class="v"></i><span class="v">48</span><span class="v">52</span><span class="v">64</span><span class="v">83</span><span class="v">98</span><span class="v">52</span><span class="v">98</span><span class="v">120</span><span class="v">126</span><span class="v">149</span></div>
    <div class="grid wrow light"><i class="v"></i><span class="v">52</span><span class="v">56</span><span class="v">68</span><span class="v">90</span><span class="v">106</span><span class="v">56</span><span class="v">106</span><span class="v">126</span><span class="v">132</span><span class="v">157</span></div>
    <div class="grid wrow dark"><i class="v"></i><span class="v">56</span><span class="v">60</span><span class="v">72</span><span class="v">98</span><span class="v">113</span><span class="v">60</span><span class="v">113</span><span class="v">132</span><span class="v">138</span><span class="v">165</span></div>
    <div class="grid wrow light"><i class="v"></i><span class="v">60</span><span class="v">64</span><span class="v">76</span><span class="v">106</span><span class="v">120</span><span class="v">64</span><span class="v">120</span><span class="v">145</span><span class="v">144</span><span class="v">174</span></div>
    <div class="grid wrow dark"><i></i><span class="v">HWT</span><span class="v">68</span><span class="v">80</span><span class="v">113</span><span class="v">126</span><span class="v">68</span><span class="v">126</span><span class="v">152</span><span class="v">150</span><span class="v">184</span></div>
    <div class="grid wrow light"><i></i><i></i><span class="v">72</span><span class="v">84</span><span class="v">120</span><span class="v">132</span><span class="v">72</span><span class="v">132</span><span class="v">165</span><span class="v">157</span><span class="v">197</span></div>
    <div class="grid wrow dark"><i></i><i></i><span class="v">76</span><span class="v">88</span><span class="v">126</span><span class="v">138</span><span class="v">76</span><span class="v">138</span><span class="v">185</span><span class="v">165</span><span class="v">215</span></div>
    <div class="grid wrow light"><i></i><i></i><span class="v">80</span><span class="v">92</span><span class="v">132</span><span class="v">144</span><span class="v">80</span><span class="v">144</span><span class="v">235</span><span class="v">175</span><span class="v">285</span></div>
    <div class="grid wrow dark"><i></i><i></i><span class="v">84</span><span class="v">96</span><span class="v">138</span><span class="v">150</span><span class="v">84</span><span class="v">150</span><i class="v"></i><span class="v">190</span><i></i></div>
    <div class="grid wrow light"><i></i><i></i><span class="v">88</span><span class="v">100</span><span class="v">144</span><span class="v">157</span><span class="v">88</span><span class="v">157</span><i class="v"></i><span class="v">215</span><i></i></div>
    <div class="grid wrow dark"><i></i><i></i><span class="v">92</span><span class="v">110</span><span class="v">150</span><span class="v">165</span><span class="v">92</span><span class="v">165</span><i class="v"></i><span class="v">285</span><i></i></div>
    <div class="grid wrow light"><i></i><i></i><span class="v">HWT</span><span class="v">HWT</span><span class="v">157</span><span class="v">175</span><span class="v">96</span><span class="v">175</span><i></i><i></i><i></i></div>
    <div class="grid wrow dark"><i></i><i></i><i></i><i></i><span class="v">165</span><span class="v">190</span><span class="v">100</span><span class="v">190</span><i></i><i></i><i></i></div>
    <div class="grid wrow light"><i></i><i></i><i></i><i></i><span class="v">175</span><span class="v">215</span><span class="v">110</span><span class="v">215</span><i></i><i></i><i></i></div>
    <div class="grid wrow dark"><i></i><i></i><i></i><i></i><span class="v">190</span><span class="v">HWT</span><span class="v">120</span><span class="v">HWT</span><i></i><i></i><i></i></div>
    <div class="grid wrow light"><i></i><i></i><i></i><i></i><span class="v">HWT</span><i class="v"></i><span class="v">130</span><i></i><i></i><i></i><i></i></div>
  </div>

  <div class="art mats" role="img" aria-label="Overhead view of wrestling mats in an arena"></div>
  <div class="art singlets" role="img" aria-label="Custom champion singlets"></div>
  <div class="abs awards-band"></div>
  <div class="art warrior" role="img" aria-label="Armoured warrior with crested helmet and spear"></div>
  <div class="abs awards">
    <h2>Custom singlets are awarded</h2>
    <p>To champions in all weight classes, Excluding the high school and Open division.</p>
  </div>
</section>

</body>
</html>
```